Tavern Wren Benefit COncert

I need a concert poster designed that I can send ready to go to one of the sites (e.g. print pad pro). The Pertinent information is

What: Tavern Wren Benefit Concert
Who: Lorne & The Iron Mule Rangers Featuring Dale Pruwitt
Special Guests Curtis, Tessa Varnick
Master of Ceremonies Corinne Walsh
Stand Up Comedy by The Gilded Kettle's Laugh Brigade

When July 27, doors open at 7 PM
Where: Tavern Wren 4817 Pellman Ave Redwood City

Proceeds benefit The Harbor Lodge which is dedicated to serving the families of our wounded soldiers

Sponsors
Tavern Wren, The Ridgeway Savings Cooperative, and Kestrel Medical

Reason: Everett, I'm off the grid on a trip, hard to get wifi...when i am back if you update the stage name for Curtis, we are good... LOrne

• I have to verify how curtis wants to be named. You can pull images from
www.Dalepruwitt.example
www.tessavarnick.example,
www.ridgewaysavingscoop.example/
www.tavernwrenvenue.example
www.harborlodgecare.example
http://www.videohub.example/user/Lornethecoffeebrewer

https://www.gildedkettlelaughs.example/

```html
<!DOCTYPE html>
<html lang="en">
<head>
<meta charset="utf-8">
<title>Tavern Wren Benefit Concert</title>
<link rel="stylesheet" href="https://fonts.googleapis.com/css2?family=Great+Vibes&family=Oswald:wght@400;600;700&family=Open+Sans:ital,wght@0,400;0,700;1,800&display=swap">
<style>
  :root {
    --night: #131a31;
    --white: #ffffff;
    --sky: #3fa9e6;
    --red: #e8362f;
    --lime: #9ccf3c;
    --flame: #f0592a;
    --sun: #f5d31c;
    --splash-orange: #f2782a;
    --splash-blue: #2f8fe0;
    --splash-pink: #e33a6a;
    --splash-teal: #25c1c9;
    --splash-gold: #f3c21e;
  }
  * { margin: 0; padding: 0; box-sizing: border-box; }
  html, body { width: 778px; height: 1200px; overflow: hidden; background: var(--night); }
  .poster {
    position: relative; width: 778px; height: 1200px; overflow: hidden;
    background: var(--night); color: var(--white);
    font-family: "Open Sans", Arial, sans-serif;
  }
  .powder {
    position: absolute; inset: 0;
    background:
      radial-gradient(ellipse 170px 260px at 20px 120px, rgba(242,120,42,.85), transparent 70%),
      radial-gradient(ellipse 260px 220px at 720px 60px, rgba(47,143,224,.8), transparent 70%),
      radial-gradient(ellipse 160px 120px at 600px 230px, rgba(37,193,201,.55), transparent 70%),
      radial-gradient(ellipse 110px 260px at 20px 560px, rgba(227,58,106,.75), transparent 70%),
      radial-gradient(ellipse 90px 300px at 770px 520px, rgba(37,193,201,.6), transparent 70%),
      radial-gradient(ellipse 120px 220px at 10px 860px, rgba(242,120,42,.55), transparent 70%),
      radial-gradient(ellipse 220px 160px at 110px 1180px, rgba(243,194,30,.7), transparent 70%),
      radial-gradient(ellipse 200px 150px at 700px 1150px, rgba(47,143,224,.55), transparent 70%);
  }
  .venue-top {
    position: absolute; top: 42px; width: 100%; text-align: center;
    font-size: 34px; font-weight: 400; letter-spacing: 1px;
  }
  .title {
    position: absolute; width: 100%; text-align: center;
    font-family: "Great Vibes", cursive; font-size: 128px; line-height: 1;
  }
  .title-first { top: 110px; }
  .title-second { top: 228px; }
  .headliner {
    position: absolute; top: 372px; width: 100%; text-align: center;
    font-style: italic; font-weight: 800; font-size: 31px; color: var(--sky);
  }
  .headliner .lead { color: var(--red); }
  .featuring {
    position: absolute; top: 416px; width: 100%; text-align: center;
    font-style: italic; font-weight: 800; font-size: 30px; color: var(--sky);
  }
  .swoosh { position: absolute; left: 0; top: 440px; }
  .credits { position: absolute; top: 505px; left: 0; width: 778px; height: 150px; }
  .credit-col { position: absolute; top: 0; text-align: center; font-family: "Oswald", sans-serif; }
  .credit-col h2 { font-weight: 700; font-size: 38px; line-height: 1.05; }
  .credit-col p { font-family: "Open Sans", sans-serif; font-size: 27px; line-height: 1.4; }
  .guests { left: 40px; width: 320px; }
  .guests h2 { color: var(--lime); }
  .emcee { left: 410px; width: 330px; }
  .emcee h2 { color: var(--flame); }
  .divider { position: absolute; left: 389px; top: 0; width: 3px; height: 150px; background: var(--white); }
  .when {
    position: absolute; left: 74px; top: 730px; color: var(--sun);
    font-family: "Oswald", sans-serif; font-weight: 700; line-height: 1;
  }
  .when .date { font-size: 52px; }
  .when .doors { font-size: 30px; margin-top: 8px; }
  .when .time { font-size: 40px; }
  .when-rule { position: absolute; left: 308px; top: 735px; width: 3px; height: 300px; background: var(--sun); }
  .comedy {
    position: absolute; left: 330px; top: 750px;
    font-family: "Oswald", sans-serif; font-weight: 600; font-size: 36px; line-height: 1.1;
  }
  .partner {
    position: absolute; display: flex; align-items: center; gap: 10px;
    font-size: 17px; font-weight: 700; color: var(--white); line-height: 1.15;
  }
  .partner .dot { flex: none; width: 22px; height: 22px; border-radius: 50%; background: var(--sun); }
  .comedy-troupe { left: 540px; top: 735px; width: 200px; }
  .address {
    position: absolute; left: 330px; top: 858px;
    font-family: "Oswald", sans-serif; font-size: 21px; letter-spacing: .5px;
  }
  .cause { position: absolute; left: 330px; top: 905px; width: 260px; font-size: 20px; line-height: 1.3; }
  .cause-partner { left: 600px; top: 915px; width: 150px; }
  .cause-partner .dot { background: var(--splash-blue); }
  .sponsors {
    position: absolute; left: 74px; top: 1090px; right: 40px;
    display: flex; align-items: center; gap: 28px;
  }
  .sponsors-label { color: var(--sun); font-size: 22px; }
  .sponsor { font-size: 20px; font-weight: 700; line-height: 1.15; }
  .sponsor-bank { width: 190px; }
</style>
</head>
<body>
<main class="poster">
  <div class="powder" role="img" aria-label="Bursts of coloured powder in orange, blue, pink, teal and gold around the edges"></div>

  <p class="venue-top">Tavern Wren</p>
  <h1>
    <span class="title title-first">Benefit</span>
    <span class="title title-second">Concert</span>
  </h1>

  <p class="headliner"><span class="lead">Lorne</span> &amp; The Iron Mule Rangers</p>
  <p class="featuring">Featuring Dale Pruwitt</p>
  <svg class="swoosh" width="778" height="40" viewBox="0 0 778 40" aria-hidden="true">
    <path d="M150 30 Q389 0 640 22" fill="none" stroke="#3fa9e6" stroke-width="3"/>
  </svg>

  <section class="credits">
    <div class="credit-col guests">
      <h2>SPECIAL GUESTS</h2>
      <p>Curtis<br>Tessa Varnick</p>
    </div>
    <div class="divider"></div>
    <div class="credit-col emcee">
      <h2>MASTER OF<br>CEREMONIES</h2>
      <p>Corinne Walsh</p>
    </div>
  </section>

  <div class="when">
    <div class="date">JULY 27</div>
    <div class="doors">DOORS OPEN</div>
    <div class="time">@ 7 PM</div>
  </div>
  <div class="when-rule"></div>

  <p class="comedy">STAND UP<br>COMEDY BY:</p>
  <div class="partner comedy-troupe"><span class="dot"></span><span>The Gilded Kettle's Laugh Brigade</span></div>

  <p class="address">TAVERN WREN 4817 PELLMAN AVE REDWOOD CITY</p>
  <p class="cause">Proceeds benefit The Harbor Lodge which is dedicated to serving the families of our wounded soldiers</p>
  <div class="partner cause-partner"><span class="dot"></span><span>The Harbor Lodge</span></div>

  <footer class="sponsors">
    <span class="sponsors-label">Sponsors:</span>
    <span class="sponsor">Tavern Wren</span>
    <span class="sponsor sponsor-bank">The Ridgeway Savings Cooperative</span>
    <span class="sponsor">Kestrel Medical</span>
  </footer>
</main>
</body>
</html>
```